BRIM Outreach Partners Business Card Rebrand

Hello Designers! We are looking for help designing our new business card to go in conjunction with our company rebrand. Unfortunately, we have an event mid June that requires we get these printed ASAP (before our new website is launched.) We have a mostly complete Brand Book which I have uploaded to this request for your reference to company information, style, fonts. I've also enclosed our logo file in .eps & .jpg. Attached is a sample business card my boss liked but said was "too simple." I made it in Canva and do not profess to be a designer. NOT FOR DESIGN REFERENCE, ONLY FOR CONTEXT Here is what our old website looks like: https://brimoutreachpartners.com/.

```html
<!DOCTYPE html>
<html lang="en">
<head>
<meta charset="utf-8">
<title>BRIM Outreach Partners – Business Card</title>
<link rel="stylesheet" href="https://fonts.googleapis.com/css2?family=Questrial&display=swap">
<style>
  :root {
    --stage: #c4c4c4;
    --brand-blue: #4ab3e3;
    --brand-blue-deep: #4aa6d2;
    --brand-blue-soft: #9fd4ee;
    --ink: #111111;
    --paper: #ffffff;
  }
  * { box-sizing: border-box; margin: 0; padding: 0; }
  html, body {
    width: 1200px; height: 1200px; overflow: hidden;
    background: var(--stage);
    font-family: "Questrial", "Century Gothic", sans-serif;
  }
  .card {
    position: absolute; left: 162px; width: 876px; height: 512px; overflow: hidden;
  }
  .card--front { top: 69px; background: var(--brand-blue); color: var(--paper); }
  .card--back  { top: 622px; background: var(--paper); }

  .front-swoosh { position: absolute; inset: 0; width: 100%; height: 100%; }

  .brand { position: absolute; display: flex; align-items: center; }
  .brand__dot { border-radius: 50%; flex: none; }
  .brand__name { color: var(--ink); white-space: nowrap; line-height: 1; font-weight: 400; }

  .card--front .brand { left: 69px; top: 62px; gap: 20px; }
  .card--front .brand__dot { width: 104px; height: 104px; background: var(--paper); }
  .card--front .brand__name { font-size: 33px; }

  .person { position: absolute; right: 72px; top: 234px; text-align: right; }
  .person__name { font-size: 37px; font-weight: 400; line-height: 1; letter-spacing: 0.2px; }
  .person__role { margin-top: 14px; font-size: 19px; font-weight: 400; letter-spacing: 2.5px; text-transform: uppercase; }

  .contact { position: absolute; right: 72px; top: 356px; list-style: none; text-align: right; }
  .contact__item {
    display: flex; justify-content: flex-end; align-items: center; gap: 16px;
    font-size: 21px; line-height: 34px;
  }
  .contact__icon { width: 15px; height: 15px; fill: var(--paper); flex: none; }

  .back-texture {
    position: absolute; inset: 0;
    background:
      radial-gradient(ellipse 60% 70% at 50% 55%, var(--paper) 55%, rgba(255,255,255,0) 100%),
      linear-gradient(135deg, var(--brand-blue-soft), #e6f4fb 45%, #e6f4fb 55%, var(--brand-blue-soft));
  }
  .card--back .brand { left: 50%; top: 50%; transform: translate(-50%, -50%); gap: 24px; }
  .card--back .brand__dot { width: 140px; height: 140px; background: var(--brand-blue); }
  .card--back .brand__name { font-size: 40px; }
</style>
</head>
<body>

<section class="card card--front" aria-label="Business card front">
  <svg class="front-swoosh" viewBox="0 0 876 512" preserveAspectRatio="none" aria-hidden="true">
    <path d="M876,160 C620,165 330,260 0,512 L876,512 Z" fill="var(--brand-blue-deep)"/>
    <path d="M110,390 C250,300 420,260 560,250 C420,275 260,320 110,390 Z" fill="var(--brand-blue)" opacity="0.55"/>
  </svg>

  <div class="brand">
    <span class="brand__dot"></span>
    <span class="brand__name">BRIM Outreach Partners</span>
  </div>

  <div class="person">
    <h1 class="person__name">Daniel Marsh-Whitley</h1>
    <p class="person__role">Managing Partner</p>
  </div>

  <ul class="contact">
    <li class="contact__item">+945-555-0147
      <svg class="contact__icon" viewBox="0 0 24 24" aria-hidden="true"><path d="M6.6 10.8a15.1 15.1 0 0 0 6.6 6.6l2.2-2.2a1 1 0 0 1 1-.25 11.4 11.4 0 0 0 3.6.6 1 1 0 0 1 1 1V20a1 1 0 0 1-1 1A17 17 0 0 1 3 4a1 1 0 0 1 1-1h3.5a1 1 0 0 1 1 1c0 1.25.2 2.45.6 3.6a1 1 0 0 1-.25 1z"/></svg>
    </li>
    <li class="contact__item">daniel@brimoutreachpartners.com
      <svg class="contact__icon" viewBox="0 0 24 24" aria-hidden="true"><rect x="2" y="5" width="20" height="14" rx="1.5"/><path d="M3 6.5l9 6.5 9-6.5" fill="none" stroke="var(--brand-blue-deep)" stroke-width="2"/></svg>
    </li>
    <li class="contact__item">Denver, CO based (Mountain Time)
      <svg class="contact__icon" viewBox="0 0 24 24" aria-hidden="true"><path d="M12 2a7 7 0 0 0-7 7c0 5.2 7 13 7 13s7-7.8 7-13a7 7 0 0 0-7-7zm0 9.5A2.5 2.5 0 1 1 12 6.5a2.5 2.5 0 0 1 0 5z"/></svg>
    </li>
  </ul>
</section>

<section class="card card--back" aria-label="Business card back">
  <div class="back-texture" role="img" aria-label="Light blue halftone dot texture fading toward the centre"></div>
  <div class="brand">
    <span class="brand__dot"></span>
    <span class="brand__name">BRIM Outreach Partners</span>
  </div>
</section>

</body>
</html>
```